User profile management app in Bootstrap & AngularJS

We have a single page web app with front end built on AngularJS and Bootstrap. There is a navbar on top and about 10 different views (user profile view, user profile edit, update-able list of items, help section, ...). At this point the app has functionality but no graphics or thought-out layout.

Need a designer to take the existing HTML, CSS (or even JS) files and modify and expand them to make the app look good. Find the existing HTML and JS files for the client attached. You'll need to download angular, bootstrap and ng-map libraries separately.

You can experience the code live at https://design.kelvo.net/kelvoportal.html

The templates provided are text-only but the result should contain a few icons for better visual experience. Some suggested areas for images include device types (email, cell phone, pager, landline phone, ...), status indicators (true/false, on/off, enabled/disabled, ...), navigation (expand/collapse, previous page/next page, ...), file download, CRUD management (add, edit, delete), help popups, etc

The resulting design and code should be mobile-friendly and handicap-accessible (Section 508 compliant).

Font desired: Univers family but not required, otherwise Arial
Only use color from the list provided in the attached file. Colors should not indicate a specific meaning and the whole design should be primarily blue (RGB R0 G103 B198) and white themed.

Allow for banner somewhere on top of page - about 530 x 100 pixels. Allow for a footer with an image on the left and 2-3 sentences of text (copyright, disclaimer, etc).
Updates

Target Market(s)

general public, design for simplicity and ease of use

Industry/Entity Type

Cell Phone

Coding

Coded - Design and coding required

Number of Pages Required

5+ page

Font styles to use
Sans Serif
Other font styles liked:
• Univers family preferred not required otw Arial

Requirements
Must have
• Use blue (RGB R0 G103 B198) and white theme. Must be mobile friendly and handicap-enabled.
• Icons: Use the three stroke weights; light, medium, bold.
• Icons can be designed as outlines or solid silhouettes in two-dimensional form. Icons must be recognizable to a majority of the intended audience. Avoid fine lines and overly complex imagery.

```html
<!DOCTYPE html>
<html lang="en">
<head>
<meta charset="utf-8">
<title>User Profile Management – Profile</title>
<link href="https://fonts.googleapis.com/css2?family=Open+Sans:wdth,wght@75..100,400..700&display=swap" rel="stylesheet">
<style>
  :root {
    --page-bg: #cfe8f6;
    --brand-blue: #0067c6;
    --brand-red: #a0103a;
    --action-green: #37a033;
    --panel-bg: #f3f9fc;
    --label-blue: #1a6fc9;
    --value-red: #c43a3a;
    --heading-red: #d95f5f;
    --button-red: #cf2f3b;
    --rule: #d9b8c2;
    --white: #ffffff;
  }
  * { box-sizing: border-box; margin: 0; padding: 0; }
  html, body { width: 1200px; height: 1000px; overflow: hidden; }
  body {
    position: relative;
    background: var(--page-bg);
    font-family: "Open Sans", Arial, sans-serif;
  }
  .brand { position: absolute; left: 203px; top: 84px; display: flex; align-items: center; gap: 8px; }
  .brand-dot { width: 20px; height: 20px; border-radius: 50%; background: var(--brand-blue); }
  .brand-name { color: var(--brand-blue); font-size: 21px; font-weight: 400; line-height: 1.1; width: 150px; }

  .btn-green {
    position: absolute; background: var(--action-green); color: var(--white);
    border-radius: 3px; font-size: 12px; font-weight: 700; font-stretch: 88%;
    display: flex; align-items: center; justify-content: space-between; padding: 0 6px;
  }
  .search { left: 407px; top: 55px; width: 176px; height: 28px; padding: 0 10px 0 9px; }
  .login { left: 407px; top: 108px; width: 82px; height: 28px; }
  .register { left: 499px; top: 108px; width: 82px; height: 28px; }

  .banner {
    position: absolute; left: 613px; top: 55px; width: 379px; height: 81px;
    background: linear-gradient(90deg, #3e8f2f, #9bd36b 40%, #6fb04a);
    box-shadow: 3px 3px 6px rgba(0,0,0,0.25);
  }

  .main-nav {
    position: absolute; left: 0; top: 180px; width: 1200px; height: 41px;
    background: var(--brand-blue);
  }
  .main-nav a {
    position: absolute; top: 0; height: 41px; line-height: 40px;
    color: var(--white); text-decoration: none;
    font-size: 17px; font-weight: 600; font-stretch: 85%;
  }
  .main-nav a.active {
    top: 2px; height: 37px; line-height: 36px; width: 70px; text-align: center;
    background: linear-gradient(#ffffff, #d9e6ef); color: var(--brand-red);
    box-shadow: 2px 2px 4px rgba(0,0,0,0.35);
  }

  .panel {
    position: absolute; left: 224px; top: 269px; width: 754px; height: 740px;
    background: var(--panel-bg); box-shadow: 3px 0 4px rgba(0,0,0,0.18);
  }
  .panel-title {
    position: absolute; left: 69px; top: 18px; width: 143px; height: 43px;
    background: var(--heading-red); color: var(--white); border: 1px solid #b84a4a;
    font-size: 20px; font-weight: 600; font-stretch: 90%; text-align: center; line-height: 41px;
    box-shadow: 2px 3px 4px rgba(0,0,0,0.3);
  }
  .field { position: absolute; left: 21px; width: 712px; height: 20px; border-bottom: 1px solid var(--rule); }
  .field-label { position: absolute; left: 48px; top: 5px; font-size: 14px; line-height: 19px; color: var(--label-blue); white-space: nowrap; }
  .field-value { position: absolute; left: 247px; top: 3px; font-size: 14px; line-height: 19px; color: var(--value-red); display: flex; align-items: center; gap: 10px; }

  .tag-input {
    position: absolute; left: 242px; top: -16px; width: 352px; height: 35px;
    background: var(--white); border: 1px solid #dde3e8;
  }
  .tag {
    position: absolute; left: 3px; top: 2px; width: 120px; height: 30px;
    background: #eef1f3; border: 1px solid #cdd2d6; border-radius: 2px;
    display: flex; align-items: center; gap: 6px; padding-left: 16px;
    color: var(--value-red); font-size: 14px;
  }
  .tag-remove { position: absolute; right: 4px; top: 0; font-size: 12px; color: #777; }

  .update {
    position: absolute; left: 342px; top: 417px; width: 71px; height: 21px;
    background: var(--button-red); color: var(--white); font-size: 12px; text-align: center;
    line-height: 21px; border-radius: 3px; box-shadow: 2px 2px 4px rgba(0,0,0,0.3);
  }
</style>
</head>
<body>
  <header>
    <div class="brand"><span class="brand-dot"></span><span class="brand-name">User Profile Management</span></div>

    <div class="btn-green search">Search...
      <svg width="10" height="10" viewBox="0 0 10 10"><path d="M3 1l4 4-4 4" stroke="#fff" stroke-width="2" fill="none"/></svg>
    </div>
    <div class="btn-green login">Log in
      <svg width="18" height="18" viewBox="0 0 18 18"><circle cx="9" cy="9" r="8" fill="#fff"/><path d="M4 9h8M9 5l4 4-4 4" stroke="#37a033" stroke-width="2" fill="none"/></svg>
    </div>
    <div class="btn-green register">Register
      <svg width="18" height="16" viewBox="0 0 18 16"><rect x="1" y="3" width="12" height="12" fill="none" stroke="#fff" stroke-width="1.5"/><path d="M7 10l8-8 2 2-8 8H7z" fill="#fff"/></svg>
    </div>

    <div class="banner" role="img" aria-label="Banner illustration of people running across green gears"></div>
  </header>

  <nav class="main-nav">
    <a class="active" href="#" style="left:213px">Home</a>
    <a href="#" style="left:299px">Services</a>
    <a href="#" style="left:387px">Locations</a>
    <a href="#" style="left:488px">Profiles</a>
    <a href="#" style="left:575px">subscriptions</a>
    <a href="#" style="left:704px">Alertlog</a>
    <a href="#" style="left:788px">Help</a>
  </nav>

  <main class="panel">
    <h1 class="panel-title">Profile</h1>

    <div class="field" style="top:82px"><span class="field-label">First Name</span><span class="field-value">John</span></div>
    <div class="field" style="top:132px"><span class="field-label">Last Name</span><span class="field-value">Smith</span></div>
    <div class="field" style="top:182px"><span class="field-label">Contact e-mail Address</span><span class="field-value">admin</span></div>
    <div class="field" style="top:231px"><span class="field-label">City</span><span class="field-value">Gotham</span></div>
    <div class="field" style="top:280px"><span class="field-label">State</span>
      <span class="field-value">ALASKA
        <svg width="14" height="8" viewBox="0 0 14 8"><path d="M0 0h14L7 8z" fill="#c43a3a"/></svg>
      </span>
    </div>
    <div class="field" style="top:330px"><span class="field-label">Languages</span>
      <div class="tag-input">
        <div class="tag">
          <svg width="24" height="16" viewBox="0 0 24 16"><rect width="8" height="16" fill="#1f3f9a"/><rect x="8" width="8" height="16" fill="#f2c200"/><rect x="16" width="8" height="16" fill="#d2102f"/></svg>
          Chinese<span class="tag-remove">×</span>
        </div>
      </div>
    </div>

    <div class="update">Update</div>
  </main>
</body>
</html>
```